Präsentationsvorlagen für Verkaufsgespräche
Zielgruppe
Wir verkaufen hochwertigen Kaffee, der traditionel im Trommelröster langsam geröstet wird. Unsere Zielgruppe sind W/ M 30-70.
Aufgabenstellung
Mit dieser Vorlage möchte ich bei den ersten Verkaufsgesprächen unsere Firma gut repräsentieren. Das wird keine lange Präsentation, soll aber einen ansprechenden Einstieg ins Gespräch sein.
Ein paar Fotos habe ich beigefügt. Texte füge ich später ein, wenn jemand was griffbereit hat, nehme ich aber auch das gerne.

```html
<!DOCTYPE html>
<html lang="de">
<head>
<meta charset="utf-8">
<title>Ondino Cafe – Präsentationsvorlage</title>
<link rel="stylesheet" href="https://fonts.googleapis.com/css2?family=Hind:wght@400;500;600;700&family=Open+Sans:wght@300;400;600&display=swap">
<style>
:root{
  --page:#ececec;
  --white:#ffffff;
  --ink:#2b2b2b;
  --text:#3a3a3a;
  --dark:#444444;
  --band:#ebebeb;
  --diamond:#e6e6e6;
  --orange:#ff6f1a;
  --label:#ffffff;
  --bean-dark:#3a2418;
  --bean-mid:#6b4430;
  --bean-light:#9a6b4e;
}
*{box-sizing:border-box;margin:0;padding:0}
html,body{width:1200px;height:2181px;overflow:hidden;background:var(--page)}
body{position:relative;font-family:"Open Sans",sans-serif;color:var(--text)}
.slide-label{position:absolute;width:457px;text-align:center;font:400 16px "Open Sans",sans-serif;color:var(--label);letter-spacing:.5px}
.slide{position:absolute;background:var(--white);overflow:hidden;box-shadow:6px 8px 16px rgba(0,0,0,.18)}
.slide--small{width:457px;height:343px}
.photo{position:absolute}
.photo--beans{background:radial-gradient(ellipse at 60% 40%,var(--bean-light),var(--bean-mid) 45%,var(--bean-dark))}
.photo--espresso{background:linear-gradient(160deg,#5a4a40 0%,#8a7868 30%,#d9cfc4 60%,#f2ede8 100%)}
.photo--hands{background:radial-gradient(ellipse at 50% 55%,#6b4430,#3a2418 55%,#1e140e)}
.photo--scoop{background:radial-gradient(ellipse at 55% 40%,#7a4a30,#3b2218 50%,#1c0f0c)}
.brand{position:absolute;font-family:"Hind",sans-serif;font-weight:700;color:var(--ink);line-height:1;text-align:center;transform:translateX(-50%)}
.brand--small{font-size:17px}
.brand--light{color:var(--white)}
.rule{position:absolute;height:3px;background:var(--orange)}
.heading{position:absolute;font-family:"Hind",sans-serif;font-weight:600;color:var(--ink)}
.body-copy{position:absolute;font-size:8.6px;line-height:12.4px;color:var(--text)}
.body-copy--light{color:#f3f3f3}
.body-copy p+p{margin-top:6px}
.banner{position:absolute;left:0;top:2063px;width:1200px;height:118px;background:var(--orange);color:var(--white);font:300 62px "Open Sans",sans-serif;letter-spacing:1px;display:flex;align-items:center;justify-content:center}
</style>
</head>
<body>

<!-- Title slide -->
<div class="slide-label" style="left:371px;top:50px">SLIDE 1</div>
<section class="slide" style="left:112px;top:82px;width:976px;height:732px">
  <div class="photo photo--beans" style="left:20px;top:20px;width:936px;height:690px" role="img" aria-label="Kaffeebohnen im Trommelröster"></div>
  <div style="position:absolute;left:110px;top:126px;width:756px;height:480px;background:var(--white)">
    <div class="rule" style="left:288px;top:146px;width:180px"></div>
    <div style="position:absolute;left:0;top:168px;width:756px;height:168px;background:var(--band)"></div>
    <div class="brand" style="left:378px;top:222px;font-size:52px">Ondino</div>
    <div style="position:absolute;left:0;top:402px;width:756px;text-align:center;font:600 25px 'Open Sans',sans-serif;color:var(--ink)">Ondino Cafe</div>
    <div style="position:absolute;left:0;top:438px;width:756px;text-align:center;font:400 19px 'Open Sans',sans-serif;letter-spacing:3px;color:var(--ink)">www.ondino-kaffee.de</div>
  </div>
</section>

<!-- Slide 2 -->
<div class="slide-label" style="left:112px;top:852px">SLIDE 2</div>
<section class="slide slide--small" style="left:112px;top:886px">
  <svg style="position:absolute;left:0;top:0" width="190" height="343" role="img" aria-label="Espresso läuft aus dem Siebträger in eine Tasse">
    <defs><linearGradient id="esp" x1="0" y1="0" x2="1" y2="1"><stop offset="0" stop-color="#5a4a40"/><stop offset=".4" stop-color="#8a6a4a"/><stop offset="1" stop-color="#efe9e3"/></linearGradient></defs>
    <polygon points="0,0 130,0 186,189 117,343 0,343" fill="url(#esp)"/>
  </svg>
  <div class="brand brand--small" style="left:415px;top:52px">Ondino</div>
  <div class="rule" style="left:208px;top:134px;width:101px"></div>
  <div class="heading" style="left:208px;top:148px;width:240px;font-size:14px;line-height:18.5px">Wir verkaufen hochwertigen Kaffee, der traditionel im Trommelröster langsam geröstet wird.</div>
  <div class="body-copy" style="left:208px;top:243px;width:230px;line-height:14.8px">Lorem ipsum dolor sit amet, consectetur adipiscing elit, sed do eiusmod tempor incididunt ut labore et dolore magna aliqua. Nisi porta lorem mollis aliquam ut porttitor leo a diam. Non arcu risus quis varius quam quisque. Feugiat in fermentum posuere urna</div>
</section>

<!-- Slide 3 -->
<div class="slide-label" style="left:631px;top:852px">SLIDE 3</div>
<section class="slide slide--small" style="left:631px;top:886px">
  <svg style="position:absolute;left:0;top:0" width="457" height="343">
    <polygon points="184,-5 264,75 184,155 104,75" fill="var(--diamond)"/>
    <polygon points="73,65 179,171 73,277 -33,171" fill="var(--diamond)"/>
    <polygon points="184,150 264,230 184,310 104,230" fill="var(--diamond)"/>
    <polygon points="296,38 402,144 296,250 190,144" fill="var(--diamond)"/>
  </svg>
  <div class="photo" style="left:153px;top:16px;width:76px;height:84px;background:linear-gradient(90deg,#b8913e,#d8b868 40%,#c2472a 60%,#d35a2a)" role="img" aria-label="Kaffeepackung mit Sortenplakette"></div>
  <div class="photo" style="left:18px;top:94px;width:112px;height:96px;background:linear-gradient(90deg,#d9b882,#f0dcb0,#d4b07a)" role="img" aria-label="Drei goldene Kaffeepackungen"></div>
  <div class="photo" style="left:243px;top:98px;width:108px;height:98px;background:linear-gradient(90deg,#2a2a2e,#555560,#2a2a2e)" role="img" aria-label="Drei schwarze Kaffeepackungen"></div>
  <div class="photo" style="left:153px;top:188px;width:76px;height:84px;background:linear-gradient(90deg,#2c2a28,#6a5a52 40%,#a4173e 60%,#8c1234)" role="img" aria-label="Kaffeepackung mit Sortenplakette"></div>
  <div class="brand brand--small" style="left:414px;top:52px">Ondino</div>
  <div class="rule" style="left:337px;top:239px;width:102px"></div>
  <div class="heading" style="right:18px;top:255px;font-size:14px;text-align:right">Unsere Kaffeemarken</div>
  <div style="position:absolute;right:18px;top:284px;font:400 12px/23px 'Open Sans',sans-serif;text-align:right;color:var(--ink)">Cafe Brunella<br>Expresso Sierra Alta</div>
</section>

<!-- Slide 4 -->
<div class="slide-label" style="left:112px;top:1248px">SLIDE 4</div>
<section class="slide slide--small" style="left:112px;top:1279px">
  <div style="position:absolute;left:238px;top:0;width:219px;height:343px;background:var(--dark)"></div>
  <div class="brand brand--small brand--light" style="left:411px;top:56px">Ondino</div>
  <div class="rule" style="left:20px;top:60px;width:44px"></div>
  <div class="heading" style="left:20px;top:73px;font-size:14px">Über Kaffee</div>
  <div style="position:absolute;left:20px;top:108px;width:287px;height:210px;background:var(--white)"></div>
  <div class="photo photo--hands" style="left:20px;top:114px;width:277px;height:200px" role="img" aria-label="Hände halten geröstete Kaffeebohnen"></div>
  <div class="body-copy body-copy--light" style="left:319px;top:113px;width:125px">
    <p>Lorem ipsum dolor sit amet, consectetur adipiscing elit, sed do eiusmod tempor incididunt ut labore et dolore magna aliqua. Nisi porta lorem mollis aliquam ut porttitor leo a diam. Non arcu risus quis varius quam quisque. Feugiat in fermentum posuere urna nec tincidunt praesent semper feugiat. Diam quam nulla porttitor massa id neque aliqu</p>
    <p>am vestibulum morbi. Sed odio morbi quis commodo</p>
  </div>
</section>

<!-- Slide 5 -->
<div class="slide-label" style="left:631px;top:1248px">SLIDE 5</div>
<section class="slide slide--small" style="left:631px;top:1279px">
  <div style="position:absolute;left:0;top:0;width:106px;height:343px;background:var(--dark)"></div>
  <div style="position:absolute;left:26px;top:30px;width:284px;height:210px;background:var(--white)"></div>
  <div class="photo photo--scoop" style="left:30px;top:34px;width:277px;height:201px" role="img" aria-label="Kaffeebohnen auf einer Röstschaufel"></div>
  <div class="brand brand--small" style="left:414px;top:53px">Ondino</div>
  <div class="rule" style="left:344px;top:191px;width:44px"></div>
  <div class="heading" style="left:344px;top:204px;font-size:14px">Über Kaffee</div>
  <div class="body-copy" style="left:120px;top:256px;width:305px;text-align:center">Lorem ipsum dolor sit amet, consectetur adipiscing elit, sed do eiusmod tempor incididunt ut labore et dolore magna aliqua. Nisi porta lorem mollis aliquam ut porttitor leo a diam. Non arcu risus quis varius quam quisque. Feugiat in fermentum posuere urna nec tincidunt praesent semper feugiat. Diam quam nulla porttitor massa id neque aliqu</div>
</section>

<!-- Slide 6 -->
<div class="slide-label" style="left:112px;top:1637px">SLIDE 6</div>
<section class="slide slide--small" style="left:112px;top:1673px">
  <div class="photo photo--beans" style="left:62px;top:101px;width:395px;height:218px" role="img" aria-label="Kaffeebohnen im Trommelröster"></div>
  <div style="position:absolute;left:20px;top:23px;width:172px;height:142px;background:var(--white)"></div>
  <div style="position:absolute;left:20px;top:23px;width:168px;height:138px;background:var(--dark)"></div>
  <div class="body-copy body-copy--light" style="left:31px;top:34px;width:150px;font-size:7.4px;line-height:10.7px">
    <p>Lorem ipsum dolor sit amet, consectetur adipiscing elit, sed do eiusmod tempor incididunt ut labore et dolore magna aliqua. Nisi porta lorem mollis aliquam ut porttitor leo a diam. Non arcu risus quis varius quam quisque. Feugiat in fermentum posuere urna nec tincidunt praesent semper feugiat. Diam quam nulla porttitor massa id neque aliqu</p>
    <p>am vestibulum morbi. Sed odio morbi</p>
  </div>
  <div class="rule" style="left:217px;top:50px;width:44px"></div>
  <div class="heading" style="left:217px;top:63px;font-size:14px">Über Kaffee</div>
  <div class="brand brand--small" style="left:415px;top:57px">Ondino</div>
</section>

<!-- Slide 7 -->
<div class="slide-label" style="left:631px;top:1637px">SLIDE 7</div>
<section class="slide slide--small" style="left:631px;top:1673px">
  <div style="position:absolute;left:0;top:0;width:55px;height:343px;background:var(--dark)"></div>
  <div class="rule" style="left:14px;top:164px;width:3px;height:42px"></div>
  <div class="heading" style="left:28px;top:222px;font-size:14px;color:var(--white);transform:rotate(-90deg);transform-origin:0 0;white-space:nowrap">Über Kaffee</div>
  <div class="photo photo--espresso" style="left:55px;top:0;width:249px;height:343px" role="img" aria-label="Espresso läuft aus dem Siebträger in zwei Tassen"></div>
  <div class="brand brand--small" style="left:414px;top:57px">Ondino</div>
  <div class="body-copy" style="right:18px;top:104px;width:130px;text-align:right">
    <p>Lorem ipsum dolor sit amet, consectetur adipiscing elit, sed do eiusmod tempor incididunt ut labore et dolore magna aliqua. Nisi porta lorem mollis aliquam ut porttitor leo a diam. Non arcu risus quis varius quam quisque. Feugiat in fermentum posuere urna nec tincidunt praesent semper feugiat. Diam quam nulla porttitor massa id neque aliqu</p>
    <p>am vestibulum morbi. Sed odio morbi quis commodo odio. Varius quam quisque id diam vel quam elementum</p>
  </div>
</section>

<div class="banner">POWERPOINT TEMPLATE</div>

</body>
</html>
```